Quillmoor Farm Organic Flower Farm, Farmer Florist

I am a flower grower and florist, so I do everything from the field to the vase. I want to include my website, phone, email and instagram

```html
<!DOCTYPE html>
<html lang="en">
<head>
<meta charset="utf-8">
<title>Quillmoor Farm – Business Card</title>
<link href="https://fonts.googleapis.com/css2?family=Cinzel:wght@600&family=Arimo:wght@400&display=swap" rel="stylesheet">
<style>
  :root{
    --page:#ecebe8;
    --forest:#465e32;
    --sage:#9ab86a;
    --white:#ffffff;
    --rule:#8a9c78;
    --frost-core:#f6f1f1;
    --frost-edge:#e3d3d5;
  }
  *{margin:0;padding:0;box-sizing:border-box}
  html,body{width:1200px;height:900px;overflow:hidden;background:var(--page)}
  .card{
    position:absolute;left:100px;top:141px;width:1000px;height:617px;
    background:linear-gradient(90deg,var(--forest) 0 690px,var(--sage) 690px 100%);
    overflow:hidden;
  }
  .person{position:absolute;left:50px;top:90px;color:var(--white)}
  .person__name{font:600 35px/1 "Cinzel",serif;letter-spacing:.5px}
  .person__role{font:400 28px/1.3 "Arimo",sans-serif;margin-top:2px}
  .social{position:absolute;left:40px;top:262px;width:352px;height:64px}
  .social__rule{position:absolute;top:31px;height:1.5px;background:var(--rule)}
  .social__rule--left{left:0;width:127px}
  .social__rule--right{right:0;width:137px}
  .social__badge{
    position:absolute;left:137px;top:0;width:64px;height:64px;border-radius:50%;
    background:var(--sage);
  }
  .contact{position:absolute;left:48px;top:420px;list-style:none;color:var(--white)}
  .contact__item{display:flex;align-items:center;gap:10px;font:400 27px/38px "Arimo",sans-serif}
  .contact__icon{width:32px;height:32px;flex:none}
  .brand{
    position:absolute;left:439px;top:57px;width:500px;height:500px;border-radius:50%;
    background:radial-gradient(circle at 50% 45%,var(--frost-core) 0 55%,var(--frost-edge) 100%);
    display:flex;align-items:center;justify-content:center;
  }
  .brand__name{font:600 56px/1 "Cinzel",serif;color:var(--forest);letter-spacing:2px;margin-top:60px}
</style>
</head>
<body>
  <section class="card">
    <div class="person">
      <h1 class="person__name">ELLIOT MARSH</h1>
      <p class="person__role">Managing Director</p>
    </div>

    <div class="social" aria-label="Social profile">
      <span class="social__rule social__rule--left"></span>
      <span class="social__badge"></span>
      <span class="social__rule social__rule--right"></span>
    </div>

    <ul class="contact">
      <li class="contact__item">
        <svg class="contact__icon" viewBox="0 0 32 32" fill="none" stroke="#fff" stroke-width="2.4" stroke-linejoin="round">
          <path d="M7 4l5 1 2 6-3 2c1.5 3.5 4.5 6.5 8 8l2-3 6 2 1 5c-1 2-3 3-5 3C13 27 5 19 4 9c0-2 1-4 3-5z"/>
          <path d="M19 4a9 9 0 0 1 9 9M18 9a5 5 0 0 1 5 5"/>
        </svg>
        044-987 210 356
      </li>
      <li class="contact__item">
        <svg class="contact__icon" viewBox="0 0 32 32" fill="none" stroke="#fff" stroke-width="2.4" stroke-linejoin="round">
          <rect x="2" y="7" width="28" height="19"/>
          <path d="M2 7l14 11L30 7M2 26l10-10M30 26L20 16"/>
        </svg>
        hello@quillmoor.com
      </li>
      <li class="contact__item">
        <svg class="contact__icon" viewBox="0 0 32 32" fill="none" stroke="#fff" stroke-width="2.2">
          <circle cx="16" cy="16" r="13"/>
          <ellipse cx="16" cy="16" rx="6" ry="13"/>
          <path d="M3 16h26M5 9h22M5 23h22M16 3v26"/>
        </svg>
        www.quillmoorfarm.com
      </li>
    </ul>

    <div class="brand" role="img" aria-label="Frosted round window carrying the Quillmoor farm name">
      <span class="brand__name">QUILLMOOR</span>
    </div>
  </section>
</body>
</html>
```